Business Card Design - Construction Company

Tarrowin Construction is in need of a sharp, modern business card design that has an architectural/high fashion feel.

We are looking for a two sided card.

One side simple dark grey/black with some texture in the background. e.g. (a mosaic of simple interconnecting shapes or a shadow of the logo.) Something to draw attention and create interest.It will need to feature a large Tarrowin construction logo (files attached) in metallic gradient or plain white.

The other side should contain all of our information:

(in largest text)
Name of person
Tarrowin Construction Pty. Ltd.

Licensed builders specialising in:
- Bathrooms
- Kitchens
- Commercial interiors

(mid sized text)
Phone number
Fax number
person@tarrowinconstruction.example.au
www. tarrowinconstruction.example.au

(smaller text)
ABN: 62407938215
BSA license: xxx-xxxx
PO Box 8641 Kellsmoor QLD 4019 (address)

Target Market(s)

professional home and business owners

Industry/Entity Type

Construction

Requirements
Must have
• Must be bold, professional looking and modern.
Nice to have
• We are undecided as to what kind of printing we will go with.
Definitely square edged.
Probably high quality satin card.
We are also interested in designs that would work well on transparent or translucent plastic.
Ideally we would print two versions.
Should not have
• Nothing with an antique feel.
No wild colours. Small amounts of colour can be good in the right place.

```html
<!DOCTYPE html>
<html lang="en">
<head>
<meta charset="utf-8">
<title>Tarrowin Construction – Business Card</title>
<link rel="stylesheet" href="https://fonts.googleapis.com/css2?family=Arimo:wght@400;700&display=swap">
<style>
  :root {
    --page-bg: #ffffff;
    --frame: #000000;
    --ink-light: #ffffff;
    --ink-dark: #000000;
    --steel-dark: #2a2c2d;
    --steel-mid: #5d6163;
    --steel-light: #8f9395;
    --steel-pale: #b9bcbd;
    --card-edge: #111111;
  }
  * { margin: 0; padding: 0; box-sizing: border-box; }
  html, body {
    width: 1200px;
    height: 900px;
    overflow: hidden;
    background: var(--page-bg);
    font-family: "Arimo", Arial, sans-serif;
  }
  .presentation {
    position: relative;
    width: 1200px;
    height: 900px;
    border: 2px solid var(--frame);
    background: var(--page-bg);
  }

  /* Front of card */
  .card-front {
    position: absolute;
    left: 76px;
    top: 116px;
    width: 368px;
    height: 654px;
    border: 2px solid var(--card-edge);
    background: linear-gradient(160deg, var(--steel-mid) 0%, var(--steel-light) 35%, var(--steel-dark) 70%, var(--steel-mid) 88%, var(--steel-pale) 100%);
    overflow: hidden;
  }
  .mark-area {
    position: absolute;
    left: 0;
    top: 40px;
    width: 330px;
    height: 560px;
    background: radial-gradient(closest-side, rgba(205,212,214,0.55) 0%, rgba(150,158,160,0.3) 50%, rgba(120,126,128,0) 100%);
  }
  .wordmark {
    position: absolute;
    left: 258px;
    top: 18px;
    height: 470px;
    writing-mode: vertical-rl;
    transform: rotate(180deg);
    text-align: end;
    font-size: 42px;
    line-height: 1.05;
    font-weight: 700;
    letter-spacing: 3px;
    color: var(--ink-dark);
    text-transform: uppercase;
    white-space: nowrap;
  }
  .wordmark span { display: block; }
  .front-web {
    position: absolute;
    left: 14px;
    bottom: 12px;
    font-size: 17px;
    color: var(--ink-light);
    white-space: nowrap;
  }

  /* Back of card */
  .card-back {
    position: absolute;
    left: 498px;
    top: 256px;
    width: 646px;
    height: 372px;
    border: 2px solid var(--card-edge);
    background: linear-gradient(115deg, #050505 0%, #2a2b2c 30%, #6e7173 62%, #b9bbbc 100%);
    color: var(--ink-light);
    overflow: hidden;
  }
  .back-mark-area {
    position: absolute;
    left: 0;
    top: 80px;
    width: 210px;
    height: 292px;
    background: radial-gradient(closest-side, rgba(190,196,198,0.4) 0%, rgba(120,126,128,0.18) 55%, rgba(0,0,0,0) 100%);
  }
  .line {
    position: absolute;
    white-space: nowrap;
    line-height: 1;
  }
  .right { right: 26px; text-align: right; }
  .employee-name { left: 22px; top: 14px; font-size: 34px; text-transform: uppercase; }
  .company { top: 60px; font-size: 27px; }
  .licensed { top: 102px; font-size: 25px; }
  .specialties { top: 134px; font-size: 19px; }
  .contact { font-size: 21px; }
  .phone { top: 170px; }
  .fax { top: 196px; }
  .abn { top: 222px; }
  .bsa { top: 248px; }
  .postal { top: 274px; }
  .email { top: 322px; font-size: 23px; }

  .side-label {
    position: absolute;
    font-size: 22px;
    font-weight: 700;
    color: var(--ink-dark);
    transform: translateX(-50%);
  }
  .label-front { left: 260px; top: 800px; }
  .label-back { left: 814px; top: 670px; }
</style>
</head>
<body>
<main class="presentation">
  <section class="card-front" aria-label="Front of business card">
    <div class="mark-area" role="img" aria-label="Large company mark in brushed metallic steel"></div>
    <p class="wordmark"><span>Tarrowin</span><span>Construction</span></p>
    <p class="front-web">www. tarrowinconstruction.example.au</p>
  </section>
  <p class="side-label label-front">FRONT</p>

  <section class="card-back" aria-label="Back of business card">
    <div class="back-mark-area" role="img" aria-label="Company mark in brushed metallic steel"></div>
    <p class="line employee-name">Employee Name</p>
    <p class="line right company">Tarrowin Construction Pty. Ltd.</p>
    <p class="line right licensed">Licensed Builders Specialising In</p>
    <p class="line right specialties">Bathrooms, Kitchens &amp; Commercial Interiors</p>
    <p class="line right contact phone">Phone Number</p>
    <p class="line right contact fax">Fax Number</p>
    <p class="line right contact abn">ABN: 62407938215</p>
    <p class="line right contact bsa">BSA license: xxx-xxxx</p>
    <p class="line right contact postal">PO Box 8641 Kellsmoor QLD 4019</p>
    <p class="line right email">person@tarrowinconstruction.example.au</p>
  </section>
  <p class="side-label label-back">BACK</p>
</main>
</body>
</html>
```